eBook Cover

Here is the book title: 27 LESSONS EACH MINISTER SHOULD
LEARN ABOUT FINANCES

Here is the subtitle (or author section): A Harvest Lantern eBook

I've attached the harvest lantern logo below.

Target Market(s)

Church Pastors

Requirements
Must have
• Lantern Logo and Harvest Lantern color palette.
Nice to have
• I have attached some sample book covers that I like

```html
<!DOCTYPE html>
<html lang="en">
<head>
<meta charset="utf-8">
<title>27 Lessons Each Minister Should Learn About Finances</title>
<link href="https://fonts.googleapis.com/css2?family=Josefin+Sans:wght@400;600&family=Oswald:wght@300;500;700&display=swap" rel="stylesheet">
<style>
  :root {
    --sky: #7fcdd2;
    --ink: #3e484d;
    --sun: #f3ea3b;
    --sand: #dcd5cb;
  }
  * { margin: 0; padding: 0; box-sizing: border-box; }
  html, body { width: 800px; height: 1200px; overflow: hidden; }
  body { background: var(--sky); }
  .cover {
    position: relative;
    width: 800px;
    height: 1200px;
    background: var(--sky);
    overflow: hidden;
  }
  .title { position: absolute; inset: 0; }
  .title-line {
    position: absolute;
    left: 0; right: 0;
    text-align: center;
    font-family: "Josefin Sans", sans-serif;
    font-weight: 400;
    color: var(--ink);
    text-transform: uppercase;
    line-height: 1;
  }
  .title-number { top: 46px; font-size: 62px; letter-spacing: 0.42em; padding-left: 0.42em; }
  .title-key {
    top: 118px;
    font-family: "Oswald", sans-serif;
    font-weight: 700;
    font-size: 112px;
    letter-spacing: 0.02em;
    color: var(--sun);
  }
  .title-word { font-size: 64px; letter-spacing: 0.3em; padding-left: 0.3em; }
  .w1 { top: 262px; }
  .w2 { top: 340px; }
  .w3 { top: 418px; }
  .w4 { top: 496px; }
  .w5 { top: 574px; }
  .sand-band {
    position: absolute;
    left: 0; right: 0; bottom: 0;
    height: 322px;
    background: var(--sand);
  }
  .title-hero { position: absolute; left: 0; top: 640px; width: 800px; height: 300px; }
  .title-hero text {
    font-family: "Oswald", sans-serif;
    font-weight: 300;
    fill: var(--sand);
  }
  .imprint {
    position: absolute;
    left: 36px;
    top: 1000px;
    font-family: "Oswald", sans-serif;
    font-weight: 700;
    font-size: 44px;
    line-height: 1.08;
    color: var(--ink);
    text-transform: uppercase;
  }
  .publisher {
    position: absolute;
    right: 60px;
    top: 1000px;
    font-family: "Oswald", sans-serif;
    font-weight: 700;
    font-size: 44px;
    line-height: 1.08;
    color: var(--ink);
    text-transform: uppercase;
    text-align: left;
  }
</style>
</head>
<body>
  <main class="cover">
    <div class="sand-band"></div>
    <h1 class="title">
      <span class="title-line title-number">27</span>
      <span class="title-line title-key">Lessons</span>
      <span class="title-line title-word w1">Each</span>
      <span class="title-line title-word w2">Minister</span>
      <span class="title-line title-word w3">Should</span>
      <span class="title-line title-word w4">Learn</span>
      <span class="title-line title-word w5">About</span>
      <svg class="title-hero" viewBox="0 0 800 300" aria-label="Finances">
        <text x="20" y="292" font-size="380" textLength="760" lengthAdjust="spacingAndGlyphs">FINANCES</text>
      </svg>
    </h1>
    <p class="imprint">A Harvest Lantern<br>eBook</p>
    <p class="publisher">The Lantern<br>Company</p>
  </main>
</body>
</html>
```